Professional and creative business card design for recruiting service providers

Our company supports German medium-sized companies in filling vacancies promptly. For this we use social media marketing and bring our customers into the visibility.

We want a professional but also creative design for our business cards.

Please look at halvenrick-consult.de to get an impression of our CI.

Target Market(s)

Small and medium-sized companies in Germany from the industry

Industry/Entity Type

Industrie, Handwerk

Contact Information for Business Card

Name, Position, Telefonnummer, Email, Website

Colors
EE7325
F08F49
F5BC92
FAE3D3
FDF4ED

Requirements
Must have
• A picture of the employee and in the style of www.halvenrick-consult.de

```html
<!DOCTYPE html>
<html lang="de">
<head>
<meta charset="utf-8">
<title>Halvenrick Consult – Visitenkarte</title>
<link rel="stylesheet" href="https://fonts.googleapis.com/css2?family=Open+Sans:wght@400;600;700&display=swap">
<style>
  :root {
    --brand-orange: #ef5e2e;
    --backdrop: #dcdddf;
    --card-white: #ffffff;
    --text-dark: #1d1d1d;
    --text-muted: #5c5c5c;
    --logo-grey: #b9b9b9;
    --divider: #b5b5b5;
    --photo-tone-light: #d8d2cb;
    --photo-tone-dark: #4a3e38;
  }
  * { margin: 0; padding: 0; box-sizing: border-box; }
  html, body {
    width: 1200px; height: 1000px; overflow: hidden;
    background: var(--backdrop);
    font-family: "Open Sans", Arial, sans-serif;
  }
  .canvas { position: relative; width: 1200px; height: 1000px; }

  .card {
    position: absolute; left: 294px; width: 613px; height: 351px;
    border-radius: 28px;
    box-shadow: 0 28px 40px rgba(0,0,0,0.28);
  }
  .card--front { top: 82px; background: var(--brand-orange); }
  .card--back { top: 556px; background: var(--card-white); }

  /* front */
  .front-brand {
    position: absolute; left: 106px; top: 104px;
    display: flex; align-items: center; gap: 30px;
  }
  .brand-square { width: 96px; height: 96px; background: var(--card-white); }
  .brand-name {
    color: var(--card-white); font-weight: 700; font-size: 42px;
    line-height: 48px; letter-spacing: 1px;
  }
  .front-rule {
    position: absolute; left: 101px; top: 289px; width: 410px; height: 1px;
    background: rgba(255,255,255,0.55);
  }
  .front-web {
    position: absolute; left: 0; right: 0; top: 302px;
    display: flex; justify-content: center; align-items: center; gap: 6px;
    color: var(--card-white); font-size: 18px;
  }

  /* back */
  .portrait {
    position: absolute; left: 82px; top: 80px; width: 146px; height: 146px;
    border-radius: 50%;
    background: radial-gradient(circle at 50% 45%, var(--photo-tone-light) 0%, #a89484 45%, var(--photo-tone-dark) 100%);
    box-shadow: 0 8px 14px rgba(0,0,0,0.25);
  }
  .person-name {
    position: absolute; left: 0; width: 310px; top: 234px; text-align: center;
    color: var(--brand-orange); font-weight: 700; font-size: 24px; letter-spacing: -0.3px;
  }
  .person-role {
    position: absolute; left: 0; width: 310px; top: 268px; text-align: center;
    color: var(--text-dark); font-size: 15px;
  }
  .back-divider {
    position: absolute; left: 297px; top: 41px; width: 1px; height: 285px;
    background: var(--divider);
  }
  .back-brand {
    position: absolute; right: 46px; top: 38px;
    display: flex; align-items: center; gap: 8px;
  }
  .back-brand .brand-square { width: 34px; height: 34px; background: var(--logo-grey); }
  .back-brand .brand-name {
    color: var(--logo-grey); font-size: 14px; line-height: 15px; letter-spacing: 0.5px;
  }
  .contact-list { position: absolute; left: 327px; top: 127px; list-style: none; }
  .contact-item {
    display: flex; align-items: flex-start; gap: 9px;
    color: var(--text-muted); font-size: 16px; line-height: 19px;
    margin-bottom: 30px;
  }
  .contact-icon {
    flex: none; width: 30px; height: 30px; border-radius: 50%;
    background: var(--brand-orange);
    display: flex; align-items: center; justify-content: center;
  }
  .contact-item span { padding-top: 5px; }
</style>
</head>
<body>
<main class="canvas">

  <section class="card card--front">
    <div class="front-brand">
      <div class="brand-square"></div>
      <div class="brand-name">HALVENRICK<br>CONSULT</div>
    </div>
    <div class="front-rule"></div>
    <div class="front-web">
      <svg width="13" height="13" viewBox="0 0 14 14" fill="none" stroke="#fff" stroke-width="1.3">
        <circle cx="7" cy="7" r="6"/><ellipse cx="7" cy="7" rx="2.6" ry="6"/><line x1="1" y1="7" x2="13" y2="7"/>
      </svg>
      halvenrick-consult.de
    </div>
  </section>

  <section class="card card--back">
    <div class="portrait" role="img" aria-label="Porträtfoto des Mitarbeiters"></div>
    <div class="person-name">Jonas Ebeling</div>
    <div class="person-role">Senior Recruiting Berater</div>

    <div class="back-divider"></div>

    <div class="back-brand">
      <div class="brand-square"></div>
      <div class="brand-name">HALVENRICK<br>CONSULT</div>
    </div>

    <ul class="contact-list">
      <li class="contact-item">
        <div class="contact-icon">
          <svg width="14" height="14" viewBox="0 0 24 24" fill="#fff"><path d="M6.6 10.8a15.1 15.1 0 0 0 6.6 6.6l2.2-2.2c.3-.3.7-.4 1-.2 1.1.4 2.3.6 3.6.6.6 0 1 .4 1 1V20c0 .6-.4 1-1 1A17 17 0 0 1 3 4c0-.6.4-1 1-1h3.5c.6 0 1 .4 1 1 0 1.3.2 2.5.6 3.6.1.3 0 .7-.2 1z"/></svg>
        </div>
        <span>0171 394 2758</span>
      </li>
      <li class="contact-item">
        <div class="contact-icon">
          <svg width="16" height="12" viewBox="0 0 16 12" fill="none" stroke="#fff" stroke-width="1.3"><rect x="1" y="1" width="14" height="10"/><path d="M1 1l7 6 7-6"/></svg>
        </div>
        <span>info@halvenrick-consult.de</span>
      </li>
      <li class="contact-item">
        <div class="contact-icon">
          <svg width="12" height="16" viewBox="0 0 12 16" fill="#fff"><path d="M6 0a6 6 0 0 0-6 6c0 4.5 6 10 6 10s6-5.5 6-10a6 6 0 0 0-6-6zm0 8.3A2.3 2.3 0 1 1 6 3.7a2.3 2.3 0 0 1 0 4.6z"/></svg>
        </div>
        <span>Halvenrick Consult GmbH<br>Lindenhofer Straße 47b<br>70173 Stuttgart</span>
      </li>
    </ul>
  </section>

</main>
</body>
</html>
```